Business card design needed

We do excavation, cartage and contracting
I would quote like to have a picture of my digger as the whole back ground and the words on top. If that looks any good
Otherwise please feel free to come up with any other cool options

Cheers Marc

Industry/Entity Type

Business

Contact Information for Business Card

KRV Contracting
Excavation, Cartage, Contracting
Marcus Pellow
www.krv.co.nz
027 584 612
marc@krv.co.nz

```html
<!DOCTYPE html>
<html lang="en">
<head>
<meta charset="utf-8">
<title>KRV Contracting – Business Card</title>
<link href="https://fonts.googleapis.com/css2?family=Source+Sans+3:wght@400;600&display=swap" rel="stylesheet">
<style>
  :root {
    --bg: #dedede;
    --card: #f2f2f2;
    --green: #2a5626;
    --text: #3a3a3a;
    --rule: #c4c4c4;
    --photo-dark: #5a5a5a;
    --photo-mid: #9a9a9a;
    --photo-light: #c9c9c9;
  }
  * { margin: 0; padding: 0; box-sizing: border-box; }
  html, body { width: 1200px; height: 840px; overflow: hidden; background: var(--bg); }
  body { position: relative; font-family: "Source Sans 3", sans-serif; }

  .card {
    position: absolute;
    top: 270px;
    width: 455px;
    height: 258px;
    overflow: hidden;
  }
  .card--back { left: 97px; }
  .card--front { left: 644px; background: var(--card); }

  .photo-fill {
    position: absolute; inset: 0;
    background: linear-gradient(180deg, #7a7a7a 0%, #4f4f4f 10%, #6c6c6c 38%, #a5a5a5 60%, #8a8a8a 100%);
  }
  .photo-fill--faint {
    background: linear-gradient(180deg, #e0e0e0 0%, #d9d9d9 12%, #e4e4e4 40%, #ececec 65%, #e6e6e6 100%);
  }

  .brand {
    position: absolute;
    left: 42px; top: 86px;
    width: 158px; height: 90px;
    display: flex; align-items: center; justify-content: center; gap: 10px;
  }
  .brand__mark { width: 14px; height: 14px; background: var(--green); }
  .brand__name {
    font-weight: 600;
    font-size: 52px;
    letter-spacing: 1px;
    color: var(--green);
    line-height: 1;
  }

  .divider {
    position: absolute;
    left: 228px; top: 52px;
    width: 1px; height: 140px;
    background: var(--rule);
  }

  .contact { position: absolute; left: 256px; top: 72px; color: var(--text); }
  .contact__name { font-size: 16px; font-weight: 400; color: var(--green); margin-bottom: 15px; }
  .contact__company { font-size: 11px; line-height: 13px; margin-bottom: 2px; }
  .contact__list { list-style: none; font-size: 11px; line-height: 13px; }
  .contact__list li { display: flex; align-items: center; gap: 6px; }
  .contact__list svg { width: 8px; height: 8px; fill: var(--green); flex: none; }

  .footer-band { position: absolute; left: 0; bottom: 0; width: 100%; height: 14px; }
</style>
</head>
<body>

  <section class="card card--back">
    <div class="photo-fill" role="img" aria-label="Black and white photo of a compact excavator with its bucket resting on gravel above a forested valley"></div>
  </section>

  <section class="card card--front">
    <div class="photo-fill photo-fill--faint" role="img" aria-label="Faded background photo of the excavator on a gravel slope"></div>

    <div class="brand">
      <span class="brand__mark"></span>
      <span class="brand__name">KRV</span>
    </div>

    <div class="divider"></div>

    <div class="contact">
      <h1 class="contact__name">Marcus Pellow</h1>
      <p class="contact__company">KRV Contracting<br>Excavation, Cartage,<br>Contracting</p>
      <ul class="contact__list">
        <li><svg viewBox="0 0 10 10"><path d="M2 0.5 L3.8 2.6 L3 3.8 Q4 5.8 6.2 7 L7.4 6.2 L9.5 8 L8.4 9.5 Q3.5 9 0.5 1.6 Z"/></svg>027 584 612</li>
        <li><svg viewBox="0 0 10 10"><path d="M0 2 H10 V8.5 H0 Z M0.6 2.4 L5 5.6 L9.4 2.4" stroke="#f2f2f2" stroke-width="0.8"/></svg>marc@krv.co.nz</li>
        <li><svg viewBox="0 0 10 10"><circle cx="5" cy="5" r="4.6"/><path d="M0.8 5 H9.2 M5 0.5 Q2.5 5 5 9.5 M5 0.5 Q7.5 5 5 9.5" stroke="#f2f2f2" stroke-width="0.7" fill="none"/></svg>www.krv.co.nz</li>
      </ul>
    </div>

    <svg class="footer-band" viewBox="0 0 455 14" preserveAspectRatio="none">
      <rect x="0" y="1" width="238" height="3" fill="#444"/>
      <polygon points="0,6 230,6 236,1 455,1 455,14 0,14" fill="var(--green)"/>
    </svg>
  </section>

</body>
</html>
```